Business card design needed

I need a business card for a new company based in Perth, Western Australia, called KT Power Pty Ltd.

I'm the sole proprietor, and have 25 years' experience in directorship, senior commercial/business development/strategy roles in the oil & gas industry with both supermajors and junior listed companies. I also have interests in renewable energy (and am co-founder and director of a separate renewable energy start-up company). KT Power will be the vehicle for me to contract my services, principally in the oil & gas industry (although this will include directorship services to the renewable energy company). These services will include general consultancy in my areas of expertise, and contracting to provide senior management/director services to start-up or junior oil and gas companies.

I'm looking for a design that communicates professionalism, dynamism, experience, strategic skills and growth.

My Proflinker profile may also be useful context;

"I have a real passion for discovering new investment opportunities and turning them from talk into reality. Right now my focus is on oil, gas and energy ventures. I’m always on the look out for compelling new investment opportunities where I can bring my leadership and strategic insight to bear to make a real difference by delivering transformational results.

I spent 24 years with NX where I built up extensive international experience in oil, gas and energy and was a member of the company’s “fast track” development programme. As an entrepreneurial senior commercial leader, strategic thinker and tactical dealmaker I was responsible for numerous deals such as divestments, farm-ins, asset swaps, new acreage bids, unitizations, gas and LNG sales, creating billions of dollars of value for NX. These deals frequently broke new ground and/or required an innovative approach that delivered results in excess of what the business thought achievable. I have held senior executive and director roles covering Exploration & Production, Mergers & Acquisitions, Business Development, LNG Marketing, Joint Venture Management, Gas & Power and Corporate head office. International assignments included UK, Australia, Indonesia, Norway & Belgium.

I’m a member of the Guild of Global Fuel Brokers (GGFB) and the National Council of Board Officers (NCBO).

Board experience comprises four directorships and two alternate directorships of Australian companies, and directorship of a Not for Profit organisation.

Specialties
Strategy, Business Development, Mergers & Acquisitions, Joint Venture Management, Negotiation, Gas & LNG Marketing."

Target Market(s)

Oil and gas or energy companies of all sizes from large listed companies to start-ups - also service providers to the industry.

Industry/Entity Type

Oil And Gas

Contact Information for Business Card

KT Power Pty Ltd
Martin Dacombe
27C Ferncliff Road,
Holloway Vale,
WA 6999

Tel +61 400 555 817
email dacombemj@quenvol.example.au

```html
<!DOCTYPE html>
<html lang="en">
<head>
<meta charset="utf-8">
<title>KT Power Pty Ltd – Business Card</title>
<link rel="stylesheet" href="https://fonts.googleapis.com/css2?family=Michroma&family=Arimo:wght@700&display=swap">
<style>
  :root {
    --stage: #2b2b2b;
    --card-dark: #151515;
    --card-light: #ffffff;
    --brand-red: #c8202f;
    --brand-grey: #4d4d4f;
    --text-grey: #3c3c3c;
    --white: #ffffff;
  }
  * { box-sizing: border-box; margin: 0; padding: 0; }
  html, body {
    width: 1200px;
    height: 900px;
    overflow: hidden;
    background: var(--stage);
  }
  .canvas {
    position: relative;
    width: 1200px;
    height: 900px;
    display: flex;
    flex-direction: column;
    align-items: center;
    justify-content: center;
    gap: 48px;
  }
  .card {
    position: relative;
    width: 640px;
    height: 366px;
    overflow: hidden;
    box-shadow: 0 10px 30px rgba(0,0,0,0.45);
  }

  /* Back side */
  .card--back {
    background: var(--card-dark);
    display: flex;
    align-items: center;
    justify-content: center;
  }
  .brand-lockup--large {
    display: flex;
    flex-direction: column;
    align-items: flex-end;
  }
  .brand-lockup--large .brand-row {
    display: flex;
    align-items: center;
    gap: 18px;
  }
  .brand-lockup--large .brand-mark {
    width: 34px;
    height: 34px;
    background: var(--brand-red);
  }
  .brand-lockup--large .brand-name {
    font-family: "Michroma", sans-serif;
    font-size: 54px;
    letter-spacing: 1px;
    color: var(--brand-grey);
    line-height: 1;
  }
  .brand-lockup--large .brand-suffix {
    font-family: "Michroma", sans-serif;
    font-size: 16px;
    letter-spacing: 2px;
    color: var(--brand-grey);
    margin-top: 10px;
  }

  /* Front side */
  .card--front {
    background: var(--card-light);
  }
  .brand-lockup--small {
    position: absolute;
    left: 84px;
    top: 92px;
    display: flex;
    flex-direction: column;
    align-items: flex-end;
  }
  .brand-lockup--small .brand-row {
    display: flex;
    align-items: center;
    gap: 12px;
  }
  .brand-lockup--small .brand-mark {
    width: 22px;
    height: 22px;
    background: var(--brand-red);
  }
  .brand-lockup--small .brand-name {
    font-family: "Michroma", sans-serif;
    font-size: 34px;
    color: var(--brand-grey);
    line-height: 1;
  }
  .brand-lockup--small .brand-suffix {
    font-family: "Michroma", sans-serif;
    font-size: 10px;
    letter-spacing: 1.5px;
    color: var(--brand-grey);
    margin-top: 6px;
  }
  .name-band {
    position: absolute;
    left: 0;
    top: 196px;
    width: 330px;
    height: 30px;
    background: var(--brand-red);
    display: flex;
    align-items: center;
    padding-left: 84px;
  }
  .name-band__text {
    font-family: "Arimo", sans-serif;
    font-weight: 700;
    font-size: 16px;
    letter-spacing: 0.5px;
    color: var(--white);
  }
  .address {
    position: absolute;
    left: 84px;
    top: 240px;
    font-family: "Michroma", sans-serif;
    font-size: 11px;
    line-height: 16px;
    color: var(--text-grey);
  }
  .contact-list {
    position: absolute;
    left: 84px;
    top: 286px;
    list-style: none;
    font-family: "Michroma", sans-serif;
    font-size: 11px;
    line-height: 16px;
    color: var(--text-grey);
  }
  .contact-list__label {
    color: var(--brand-red);
  }
</style>
</head>
<body>
<main class="canvas">
  <section class="card card--back" aria-label="Business card back">
    <div class="brand-lockup brand-lockup--large">
      <div class="brand-row">
        <span class="brand-mark"></span>
        <span class="brand-name">KT POWER</span>
      </div>
      <span class="brand-suffix">PTY LTD</span>
    </div>
  </section>

  <section class="card card--front" aria-label="Business card front">
    <div class="brand-lockup brand-lockup--small">
      <div class="brand-row">
        <span class="brand-mark"></span>
        <span class="brand-name">KT POWER</span>
      </div>
      <span class="brand-suffix">PTY LTD</span>
    </div>

    <div class="name-band">
      <span class="name-band__text">MARTIN DACOMBE</span>
    </div>

    <p class="address">27C FERNCLIFF ROAD, HOLLOWAY VALE,<br>WA 6999 TEL</p>

    <ul class="contact-list">
      <li><span class="contact-list__label">P:</span> +61 400 555 817</li>
      <li><span class="contact-list__label">E:</span> DACOMBEMJ@QUENVOL.EXAMPLE.AU</li>
    </ul>
  </section>
</main>
</body>
</html>
```